Business Card Re-Design for a Lighting Designer

I would like my business card re-designed. It is currently high gloss and they scratch too easily. I don not think the current design lends itself well to a matte finish. I have included the current design for reference along with our company logo.
Check out our website for current branding.
http://www.brambleorchidstudio.example

Updates
Some of the top contenders are muslim and it is a holiday for them. I do not want to discriminate and would expect the same courtesy for holidays we celebrate.
Target Market(s)
Interior Designers, Architects
Contact Information for Business Card
Logo - Name, Title, Address, Telephone Number and Extension, Email
Font styles to use
Requirements
Must have
- All the information listed on the current business card. If you use Red, it needs to be the red from our logo.
Nice to have
- Vertical and Horizontal Designs will be entertained.
Should not have
- Requirements for a glossy finish...should not look too corporate since we are a design firm.

```html
<!DOCTYPE html>
<html lang="en">
<head>
<meta charset="utf-8">
<title>Bramble Orchid Studio — Business Card</title>
<link rel="stylesheet" href="https://fonts.googleapis.com/css2?family=Open+Sans:wght@300;400;600&display=swap">
<style>
  :root {
    --backdrop: #1a1a1b;
    --card: #252627;
    --brand-red: #9b0000;
    --text-light: #f2f2f2;
    --text-muted: #d9d9d9;
  }
  * { margin: 0; padding: 0; box-sizing: border-box; }
  html, body {
    width: 1200px;
    height: 912px;
    overflow: hidden;
    background: var(--backdrop);
    font-family: "Open Sans", sans-serif;
  }
  .sheet {
    width: 1200px;
    height: 912px;
    display: flex;
    flex-direction: column;
    align-items: center;
    justify-content: center;
    gap: 40px;
  }
  .card {
    position: relative;
    width: 700px;
    height: 400px;
    background: var(--card);
    overflow: hidden;
  }
  .card__band {
    position: absolute;
    left: 0; right: 0; bottom: 0;
    height: 12px;
    background: var(--brand-red);
  }
  .brand {
    display: flex;
    align-items: center;
    gap: 16px;
  }
  .brand__square {
    width: 40px;
    height: 40px;
    background: var(--brand-red);
    flex: none;
  }
  .brand__name {
    font-weight: 300;
    color: var(--text-light);
    font-size: 34px;
    line-height: 1.05;
    letter-spacing: 0.5px;
    text-transform: uppercase;
  }

  /* Front */
  .card--front .brand {
    position: absolute;
    left: 50%;
    top: 130px;
    transform: translateX(-50%);
  }
  .card--front .site {
    position: absolute;
    left: 0; right: 0;
    bottom: 54px;
    text-align: center;
    color: var(--text-light);
    font-size: 19px;
    letter-spacing: 0.5px;
  }

  /* Back */
  .card--back .brand {
    position: absolute;
    left: 60px;
    top: 150px;
  }
  .card--back .brand__name { font-size: 30px; }
  .divider {
    position: absolute;
    left: 350px;
    top: 70px;
    width: 1px;
    height: 230px;
    background: var(--brand-red);
  }
  .details {
    position: absolute;
    left: 380px;
    top: 66px;
    color: var(--text-light);
  }
  .details__name {
    color: var(--brand-red);
    font-weight: 600;
    font-size: 21px;
    line-height: 1.2;
  }
  .details__title {
    font-size: 15px;
    margin-bottom: 18px;
  }
  .details__address {
    font-size: 14px;
    line-height: 1.5;
    margin-bottom: 16px;
    font-style: normal;
  }
  .contact-list { list-style: none; }
  .contact-list li {
    display: flex;
    align-items: center;
    gap: 10px;
    font-size: 14px;
    line-height: 1.65;
  }
  .contact-list svg { width: 13px; height: 13px; flex: none; fill: var(--brand-red); }
</style>
</head>
<body>
<main class="sheet">
  <section class="card card--front" aria-label="Card front">
    <div class="brand">
      <span class="brand__square"></span>
      <span class="brand__name">Bramble<br>Orchid Studio</span>
    </div>
    <p class="site">www.brambleorchidstudio.example</p>
    <div class="card__band"></div>
  </section>

  <section class="card card--back" aria-label="Card back">
    <div class="brand">
      <span class="brand__square"></span>
      <span class="brand__name">Bramble<br>Orchid Studio</span>
    </div>
    <div class="divider"></div>
    <div class="details">
      <p class="details__name">Maren Calloway</p>
      <p class="details__title">Principal</p>
      <address class="details__address">217 Fernhill Avenue, Suite 40<br>Dayton, Ohio 45402 USA</address>
      <ul class="contact-list">
        <li>
          <svg viewBox="0 0 16 16" aria-hidden="true"><path d="M3.6 1.2l2.3 2.6-1.3 2a9 9 0 0 0 5.6 5.6l2-1.3 2.6 2.3-1.4 2.1C7.6 14.8 1.2 8.4 1.5 2.6z"/></svg>
          555.013.2480 x1
        </li>
        <li>
          <svg viewBox="0 0 16 16" aria-hidden="true"><path d="M1 3h14v10H1z M1.8 3.8L8 8.6l6.2-4.8" fill="var(--brand-red)"/><path d="M1.5 3.5L8 8.5l6.5-5" fill="none" stroke="var(--card)" stroke-width="1.2"/></svg>
          maren@brambleorchidstudio.example
        </li>
        <li>
          <svg viewBox="0 0 16 16" aria-hidden="true"><circle cx="8" cy="8" r="7"/><path d="M1 8h14M8 1c-3 3.5-3 10.5 0 14M8 1c3 3.5 3 10.5 0 14" fill="none" stroke="var(--card)" stroke-width="1"/></svg>
          www.brambleorchidstudio.example
        </li>
      </ul>
    </div>
    <div class="card__band"></div>
  </section>
</main>
</body>
</html>
```